Brightfern World Learning is to provide global summer programs in the United States through which students from the US and China share experiences, intensive learning, and each other’s cultures. The program seeks to more fully prepare both the US and Chinese students for their college education and future careers in this interdependent world. Chinese students are individually paired with US Students where they will reside US students' home for the period of the program.

Current website: Brightfern World Learning

Need to support both English and Chinese with different font.

Project Deadline Extended
Reason: Because of Thanksgiving Holidays.

Dear Designers,

In order to generate the best design, I uploaded some photos from our global summer program. Please check:

http://brightfernworldlearning.org/photos/

Colette

My company Logo just added to the project.

Sorry for the late update.

Project Deadline Extended
Reason: Due to Thanksgiving holiday, I don't have enough time to provide feedback to all the designers. Colette

Project Deadline Extended
Reason: Holiday season. Need more time for designer and myself.

Target Market(s)

Grade K to 12 students and their parents to sign up the global summer program. Majority audience are from China.

Industry/Entity Type

College

Font styles to use
Sans Serif

Colors
3277b5

Requirements
Must have
• You may check my current website for the summer program content
www.brightfernworldlearning.org
Check these two clips to see what service we provided.
http://www.vidhaven.example/watch?v=7kR3nq41xTm&feature=vh.be
https://www.vidhaven.example/watch?v=W8d2JP6h4oZ

Company Logo are included in the attachment.

Some photos from summer program: http://brightfernworldlearning.org/photos/
The website should show the students one to one relationship.
The website should show homestay part.

I want Photo Slider on each page to share the fun activities.

Each program will be provide a video clip as a summery.

The website should support font of both English and Chinese. I like to see both Chinese and English on the same page instead of switch back and forth. I can add Chinese part later if you leave the room.

Nice to have
• I have a lot of paired pictures. I am wondering if I can use collage of photos as the background.

The design should be playful and fun!

```html
<!DOCTYPE html>
<html lang="en">
<head>
<meta charset="utf-8">
<title>Brightfern World Learning</title>
<link rel="stylesheet" href="https://fonts.googleapis.com/css2?family=Arimo:wght@400;700&family=Open+Sans:wght@400;600;700&display=swap">
<style>
:root{
  --navy:#132a48;
  --navy-deep:#0c1d33;
  --footer:#102440;
  --blue:#3277b5;
  --blue-dark:#1d4f84;
  --blue-light:#4c8fcc;
  --link:#2d6fb0;
  --ink:#1c2430;
  --body:#4a4f56;
  --page:#e9eaeb;
  --white:#ffffff;
  --line:#cfd2d6;
  --foot-text:#c9d2dd;
}
*{box-sizing:border-box;margin:0;padding:0}
html,body{width:876px;height:1200px;overflow:hidden}
body{position:relative;background:linear-gradient(#f6f6f6 345px,var(--page) 1000px);font-family:"Open Sans",Arial,sans-serif;color:var(--body)}
.abs{position:absolute}
.header-band{left:0;top:0;width:876px;height:345px;background:var(--navy)}
.brand{left:110px;top:21px;display:flex;align-items:center;gap:6px}
.brand-mark{width:30px;height:30px;border-radius:50%;background:var(--white)}
.brand-name{font-family:"Arimo",Arial,sans-serif;font-size:16.5px;color:var(--white)}
.main-nav{left:367px;top:30px;width:388px;height:24px;border-radius:3px;background:linear-gradient(#4a86c2,#24598f);display:flex;font-family:"Arimo",Arial,sans-serif;font-size:9.5px;color:var(--white)}
.main-nav a{color:inherit;text-decoration:none;display:flex;align-items:center;justify-content:center;border-right:1px solid rgba(255,255,255,.18)}
.main-nav a:last-child{border:0}
.main-nav .active{background:linear-gradient(#6aa4dc,#3c7cbb)}
.lock{display:inline-block;width:8px;height:9px;margin-right:5px;background:#f2b72e;border-radius:1px;position:relative;top:1px}
.dropdown{left:467px;top:54px;width:89px;height:74px;background:var(--blue);font-size:6.6px;color:var(--white);z-index:3}
.dropdown li{list-style:none;height:19px;line-height:18px;padding-left:4px;border-bottom:1px solid rgba(255,255,255,.15);white-space:nowrap;overflow:hidden}
.slider{left:88px;top:67px;width:703px;height:278px;background:var(--white);padding:4px}
.slider-photo{width:100%;height:100%;background:linear-gradient(180deg,#8c7a6b 0%,#b59a8a 40%,#7d6f73 75%,#9a8f8f 100%)}
.slider-dots{left:663px;top:288px;width:92px;height:22px;background:var(--white);border-radius:4px;display:flex;align-items:center;justify-content:center;gap:5px}
.slider-dots i{width:8px;height:8px;border-radius:50%;background:var(--blue)}
.programs{left:122px;top:318px;width:633px;height:85px;border-radius:4px;background:linear-gradient(var(--blue-light),var(--blue-dark));display:flex;color:var(--white)}
.program{position:relative;padding:4px 0 0 19px}
.program h3{font-family:"Arimo",Arial,sans-serif;font-size:13px;font-weight:700;padding-bottom:3px;border-bottom:1px dotted rgba(255,255,255,.5);width:158px;white-space:nowrap}
.program p{font-size:7.4px;line-height:12.2px;width:158px;text-align:justify;margin-top:2px}
.more{position:absolute;font-size:6.4px;font-weight:700;text-decoration:underline;left:147px;top:71px}
.programs .more{color:var(--white)}
.welcome{left:122px;top:425px;width:418px}
.welcome h1{font-family:"Arimo",Arial,sans-serif;font-size:15px;font-weight:400;color:var(--ink)}
.welcome h1 b{font-weight:700}
.sub{font-family:"Arimo",Arial,sans-serif;font-size:10.5px;color:var(--link)}
.frame{background:var(--white);padding:3px;box-shadow:0 0 0 1px var(--line)}
.frame div{width:100%;height:100%}
.intro{left:123px;top:579px;width:415px;font-size:7.8px;line-height:12px;letter-spacing:.25px}
.read{color:var(--link);font-size:6.4px;font-weight:700;text-decoration:underline}
.divider{height:1px;background:var(--line);box-shadow:0 1px 0 var(--white)}
.post-title{font-family:"Arimo",Arial,sans-serif;font-size:14px;font-weight:400;color:var(--ink);line-height:16px}
.meta{font-family:"Arimo",Arial,sans-serif;font-size:8px;color:var(--link)}
.bubble{width:22px;height:18px;background:linear-gradient(#fff,#ddd);border:1px solid #bbb;font-size:8px;font-weight:700;color:#555;text-align:center;line-height:16px}
.bubble::after{content:"";position:absolute;left:4px;bottom:-5px;border:4px solid transparent;border-top-color:#bbb;border-left-color:#bbb}
.post-text{font-size:7.8px;line-height:12px;width:256px;letter-spacing:.25px}
.side-title{font-family:"Arimo",Arial,sans-serif;font-size:14px;font-weight:400;color:var(--ink)}
.search{left:566px;top:468px;width:189px;height:20px;border-radius:3px;background:linear-gradient(#fff,#e4e4e4);box-shadow:inset 0 0 0 1px #ccc}
.search b{position:absolute;right:0;top:0;width:69px;height:20px;border-radius:3px;background:linear-gradient(var(--blue-light),var(--blue-dark));color:var(--white);font-size:7.5px;text-align:center;line-height:20px}
.tabs{left:566px;top:507px;width:189px;height:173px;background:#f8f8f8;border:1px solid var(--line)}
.tab-row{display:flex;height:25px;font-family:"Arimo",Arial,sans-serif;font-size:9px;font-weight:700}
.tab-row span{flex:1;display:flex;align-items:center;justify-content:center;background:linear-gradient(var(--blue),var(--blue-dark));color:var(--white)}
.tab-row .on{background:var(--white);color:var(--ink)}
.tab-list{padding:6px 12px 0 9px;list-style:none}
.tab-list li{font-size:7.4px;font-weight:700;color:var(--link);height:23px;line-height:20px;border-bottom:1px solid var(--line)}
.tab-list li:last-child{border:0}
.pop{left:566px;width:190px;display:flex;align-items:center;gap:12px}
.pop .frame{width:44px;height:44px;padding:2px}
.pop p{font-size:7.6px;line-height:12.5px;color:#333}
.pop span{color:var(--link)}
.pager{left:723px;top:924px;display:flex;gap:2px}
.pager i{width:15px;height:14px;border-radius:2px;background:var(--blue-dark);display:flex;align-items:center;justify-content:center}
.footer{left:0;top:1002px;width:876px;height:170px;background:var(--footer)}
.foot-col{top:1028px;font-size:6.6px;color:var(--foot-text);letter-spacing:.3px}
.foot-col h4{font-size:7px;font-weight:700;color:#e4e9ef;margin-bottom:8px}
.foot-col li{list-style:none;height:18px}
.vsep{top:1028px;width:1px;height:112px;background:#2a4060}
.thumb{width:58px;height:38px;border:2px solid #d9d9d9}
.bottom-bar{left:0;top:1172px;width:876px;height:28px;background:var(--navy-deep);font-size:6.6px;color:var(--white);font-weight:600}
</style>
</head>
<body>
<div class="abs header-band"></div>

<header>
  <div class="abs brand"><span class="brand-mark"></span><span class="brand-name">Brightfern World Learning</span></div>
  <nav class="abs main-nav">
    <a href="#" style="width:50px">Home</a><a href="#" style="width:50px">About</a><a href="#" class="active" style="width:61px">Programs</a><a href="#" style="width:47px">Blog</a><a href="#" style="width:59px">Events</a><a href="#" style="width:57px">Contact</a><a href="#" style="width:64px"><span class="lock"></span>Login</a>
  </nav>
  <ul class="abs dropdown">
    <li>Hartwell Summer Program</li><li>Lakeside Summer Camp</li><li>Whole Year Program</li><li>Kestrel University</li>
  </ul>
</header>

<section class="abs slider"><div class="slider-photo" role="img" aria-label="Group photo of paired American and Chinese students with teachers in a school hallway"></div></section>
<div class="abs slider-dots"><i></i><i></i><i></i><i></i><i></i><i></i></div>

<section class="abs programs">
  <div class="program" style="width:204px"><h3>Hartwell Summer Program</h3><p>America's top high schools, but also the world's only a school setting where Meridian Institute School of Chinese culture has a special feeling.</p><a class="more">Read More</a></div>
  <div class="program" style="width:206px"><h3>Lakeside Summer Camp</h3><p>Want American children spend an unforgettable summer vacation? The team would like to participate in outdoor summer camp constructive it?</p><a class="more">Read More</a></div>
  <div class="program" style="width:223px"><h3>Whole Year Program</h3><p>We partner with schools, one in America and one in China, so that the students can do projects together; learning, living and having fun under teachers' guidance.</p><a class="more">Read More</a></div>
</section>

<main>
  <div class="abs welcome"><h1>Welcome to <b>Brightfern World Learning</b></h1><div class="sub">Nurture Global Citizens and Global Leaders</div></div>
  <div class="abs frame" style="left:122px;top:461px;width:417px;height:111px"><div role="img" aria-label="Students jumping on a lakeside beach in front of a city skyline" style="background:linear-gradient(#b9cbe0 0%,#8aa3bf 35%,#3d8bab 55%,#d7c7a7 85%)"></div></div>
  <p class="abs intro">Brightfern World Learning is to help American students and Chinese students to break the barriers between the two different cultures, experiences and education backgrounds by providing a global summer program in the U.S. with American students and Chinese students one to one paired, home stay in US families, intensive learning and culture adventure activities, and get them fully prepared for their college education and career developments in this interdependent world.</p>
  <a class="abs read" style="left:505px;top:643px">Read More</a>
  <div class="abs divider" style="left:122px;top:668px;width:418px"></div>

  <article>
    <h2 class="abs post-title" style="left:122px;top:684px;width:380px">Chicago Mayor Dana Whitcombe and Beijing four students in a cordial conversation</h2>
    <div class="abs meta" style="left:122px;top:720px">By ABCD EFG in : Interview , Date: February 2nd 2013</div>
    <div class="abs bubble" style="left:516px;top:707px">21</div>
    <div class="abs frame" style="left:123px;top:740px;width:139px;height:62px"><div role="img" aria-label="City official talking with four students in a reception room" style="background:linear-gradient(90deg,#3a2a26,#8a4a3e,#2c2624)"></div></div>
    <p class="abs post-text" style="left:279px;top:741px">Lorem ipsum dolor sit amet, consectetur adipisicing elit, sed do eiusmod tempor incididunt ut labore et dolore magna aliqua. Ut enim ad minim veniam, quis nostrud exercitation. Lorem ipsum dolor sit amet, consectetur adipisicing elit, sed do eiusmod tempor .........</p>
    <a class="abs read" style="left:482px;top:810px">Continue Reading</a>
  </article>
  <div class="abs divider" style="left:122px;top:831px;width:418px"></div>

  <article>
    <h2 class="abs post-title" style="left:122px;top:856px">Who is playing the best tennis?</h2>
    <div class="abs meta" style="left:122px;top:881px">By ABCD EFG in : Interview , Date: February 20th 2013</div>
    <div class="abs bubble" style="left:516px;top:870px">52</div>
    <div class="abs frame" style="left:123px;top:902px;width:139px;height:62px"><div role="img" aria-label="Group of students posing by a table tennis table" style="background:linear-gradient(90deg,#5a3a30,#b0704a,#3a2a28)"></div></div>
    <p class="abs post-text" style="left:279px;top:903px">Lorem ipsum dolor sit amet, consectetur adipisicing elit, sed do eiusmod tempor incididunt ut labore et dolore magna aliqua. Ut enim ad minim veniam, quis nostrud exercitation. Lorem ipsum dolor sit amet, consectetur adipisicing elit, sed do eiusmod tempor .........</p>
    <a class="abs read" style="left:482px;top:961px">Continue Reading</a>
  </article>
</main>

<aside>
  <h3 class="abs side-title" style="left:566px;top:429px">Sidebar content</h3>
  <div class="abs sub" style="left:566px;top:449px">Insert whatever you want here</div>
  <div class="abs search"><b>SEARCH</b></div>
  <div class="abs tabs">
    <div class="tab-row"><span class="on">Sports</span><span>Science</span><span>Literature</span></div>
    <ul class="tab-list"><li>Cheerleading Cheerleading</li><li>Gymnastics</li><li>Do-It-All Sports Camp</li><li>We Are The World</li><li>Tennis Camp</li><li>Community Teen Camp</li></ul>
  </div>
  <h3 class="abs side-title" style="left:566px;top:688px">Popular posts</h3>
  <div class="abs pop" style="top:717px"><div class="frame"><div role="img" aria-label="Two students in front of a city view" style="background:linear-gradient(#8aa0b8,#a05a5a)"></div></div><p>Lorem ipsum dolor sit Amet<br><span>21 Comments</span></p></div>
  <div class="abs pop" style="top:769px"><div class="frame"><div role="img" aria-label="Students working on a craft project" style="background:linear-gradient(#c89a7a,#7a9a6a)"></div></div><p>Lorem ipsum dolor sit Amet<br><span>52 Comments</span></p></div>
  <div class="abs pop" style="top:821px"><div class="frame"><div role="img" aria-label="Students by a lake with skyline" style="background:linear-gradient(#9ab4cc,#4a7aa0)"></div></div><p>Lorem ipsum dolor sit Amet<br><span>14 Comments</span></p></div>
  <div class="abs pop" style="top:874px"><div class="frame"><div role="img" aria-label="Two students smiling together" style="background:linear-gradient(#c8b09a,#b06080)"></div></div><p>Lorem ipsum dolor sit Amet<br><span>21 Comments</span></p></div>
  <div class="abs pager">
    <i><svg width="6" height="8" viewBox="0 0 6 8"><path d="M5 0L0 4l5 4z" fill="#fff"/></svg></i>
    <i><svg width="6" height="8" viewBox="0 0 6 8"><path d="M1 0l5 4-5 4z" fill="#fff"/></svg></i>
  </div>
</aside>

<footer>
  <div class="abs footer"></div>
  <div class="abs foot-col" style="left:121px"><h4>ALLIANCES</h4><ul><li>ALLIANCE NAME ONE</li><li>ALLIANCE NAME TWO</li><li>ALLIANCE NAME THREE</li><li>ALLIANCE NAME ONE</li><li>ALLIANCE NAME TWO</li><li>ALLIANCE NAME THREE</li></ul></div>
  <div class="abs vsep" style="left:243px"></div>
  <div class="abs foot-col" style="left:270px"><h4>SUPPORT</h4><ul><li>ONLINE SUPPORT</li><li>TELEPHONE SALES</li><li>WORKSHOPS</li><li>ONLINE SUPPORT</li><li>TELEPHONE SALES</li><li>WORKSHOPS</li></ul></div>
  <div class="abs vsep" style="left:366px"></div>
  <div class="abs foot-col" style="left:391px"><h4>DEPARTMENTS</h4><ul><li>BIOLOGY</li><li>SCIENCE</li><li>I.T.</li><li>GEOGRAPHY</li><li>SCIENCE</li><li>BUISNESS</li></ul></div>
  <div class="abs vsep" style="left:466px"></div>
  <div class="abs foot-col" style="left:494px"><h4>FROM PIXWELL</h4></div>
  <div class="abs thumb" style="left:494px;top:1052px;background:linear-gradient(135deg,#3a2418,#c0784a)" role="img" aria-label="Gallery photo"></div>
  <div class="abs thumb" style="left:558px;top:1052px;background:linear-gradient(135deg,#5a3420,#d89a6a)" role="img" aria-label="Gallery photo"></div>
  <div class="abs thumb" style="left:625px;top:1052px;background:linear-gradient(135deg,#222,#bbb)" role="img" aria-label="Gallery photo"></div>
  <div class="abs thumb" style="left:691px;top:1052px;background:linear-gradient(135deg,#444,#ccc)" role="img" aria-label="Gallery photo"></div>
  <div class="abs thumb" style="left:494px;top:1100px;background:linear-gradient(135deg,#4a2c1c,#d08858)" role="img" aria-label="Gallery photo"></div>
  <div class="abs thumb" style="left:558px;top:1100px;background:linear-gradient(135deg,#333,#aaa)" role="img" aria-label="Gallery photo"></div>
  <div class="abs thumb" style="left:625px;top:1100px;background:linear-gradient(135deg,#2a1a10,#c87040)" role="img" aria-label="Gallery photo"></div>
  <div class="abs thumb" style="left:691px;top:1100px;background:linear-gradient(135deg,#222,#ddd)" role="img" aria-label="Gallery photo"></div>
  <div class="abs bottom-bar">
    <span class="abs" style="left:121px;top:10px">HOME | ABOUT | NEWS | GALLERY | EVENTS | CONTACT</span>
    <span class="abs" style="right:121px;top:10px">© 2009 BRIGHTFERN WORLD LEARNING</span>
  </div>
</footer>
</body>
</html>
```